Front & Back Book Cover Design

Title:
THE QUIET LANDLORD: How to Grow Comfort and Plenty Through Property Held by Others
Author:
Mel T. Varnak
Design Philosophy:
A modern, minimalist-luxury aesthetic that feels visionary and intelligent — positioned between business innovation (The Brisk Venture), modern finance (The Anatomy of Thrift), and timeless real estate insight (Bold Aunt Meek Aunt).
Think: clean, bold, and idea-driven — a visual reflection of the book’s central concept: wealth through clarity, not clutter.
Back Cover:
To include book description along with author photo and bio
Files:
PNG, PDF, EPUB

```html
<!DOCTYPE html>
<html lang="en">
<head>
<meta charset="utf-8">
<title>The Quiet Landlord — Cover Spread</title>
<link href="https://fonts.googleapis.com/css2?family=Montserrat:ital,wght@0,400;0,600;0,700;0,800;1,700&family=Poppins:wght@300;400&display=swap" rel="stylesheet">
<style>
  :root {
    --stage: #2b2b2b;
    --paper: #ffffff;
    --ink: #1d1d1d;
    --brand-blue: #1a7bb0;
    --sky: #5fb4e4;
    --night: #0e1822;
    --night-soft: #23384a;
    --white: #ffffff;
  }
  * { box-sizing: border-box; margin: 0; padding: 0; }
  html, body { width: 947px; height: 1200px; overflow: hidden; background: var(--stage); }
  .spread {
    position: absolute; left: 0; top: 282px;
    width: 947px; height: 635px;
    font-family: "Montserrat", sans-serif; color: var(--ink);
  }
  .back-cover {
    position: absolute; left: 0; top: 0; width: 513px; height: 635px;
    background: var(--paper);
  }
  .front-cover {
    position: absolute; left: 513px; top: 0; width: 434px; height: 635px;
    background: radial-gradient(ellipse at 62% 42%, var(--night-soft) 0%, #16242f 45%, var(--night) 100%);
  }
  .abs { position: absolute; }

  /* title lockup: plain stacked type */
  .lockup { font-family: "Montserrat", sans-serif; }
  .lockup .article { display: block; font-weight: 600; letter-spacing: 5px; }
  .lockup .main { display: block; font-weight: 800; letter-spacing: 1px; }
  .lockup .second { display: block; font-weight: 600; }

  .back-title { left: 28px; top: 55px; width: 215px; }
  .back-title .article { font-size: 11px; line-height: 13px; color: var(--ink); }
  .back-title .main { font-size: 44px; line-height: 46px; color: var(--brand-blue); }
  .back-title .second { font-size: 14px; line-height: 16px; letter-spacing: 5.5px; color: var(--ink); }

  .house-art {
    left: 233px; top: 33px; width: 190px; height: 100px;
    background: radial-gradient(ellipse at 45% 55%, #dfe3e2 0%, #eef1f1 45%, rgba(255,255,255,0) 75%);
  }

  .copy { left: 28px; top: 136px; width: 385px; font-size: 9px; line-height: 10.5px; }
  .copy p { margin-bottom: 3.6px; }
  .copy strong { font-weight: 700; }
  .copy .lead { font-weight: 700; margin-bottom: 3px; }
  .copy .hl { color: var(--brand-blue); }
  .benefits { list-style: none; margin: 10px 0 9px; }
  .benefits li { position: relative; padding-left: 15px; margin-bottom: 4px; }
  .benefits li::before {
    content: ""; position: absolute; left: 1px; top: 3px; width: 4.5px; height: 4.5px;
    background: var(--brand-blue); transform: rotate(45deg);
  }
  .gap { margin-top: 10px; }

  .author-photo {
    left: 28px; top: 432px; width: 133px; height: 169px;
    border: 4px solid var(--brand-blue); padding: 4px; background: var(--paper);
  }
  .author-photo div {
    width: 100%; height: 100%;
    background: linear-gradient(160deg, #8a8580 0%, #5b5550 45%, #26262a 100%);
  }
  .about-label {
    left: 180px; top: 459px; width: 150px; height: 17px;
    background: var(--brand-blue); color: var(--white);
    font-size: 14px; line-height: 17px; padding-left: 7px; font-weight: 400;
  }
  .bio { left: 180px; top: 482px; width: 232px; font-size: 9.6px; line-height: 11.6px; }
  .bio strong { font-weight: 700; }

  /* spine-edge vertical title */
  .edge-title {
    left: 365px; top: 132px; width: 214px; height: 62px;
    transform: rotate(90deg); transform-origin: center;
    display: flex; flex-direction: column; justify-content: center; align-items: flex-end;
  }
  .edge-title .row { display: flex; align-items: baseline; gap: 8px; }
  .edge-title .article { font-size: 11px; color: var(--ink); letter-spacing: 4px; }
  .edge-title .main { font-size: 38px; line-height: 40px; color: var(--brand-blue); }
  .edge-title .second { font-size: 11px; line-height: 14px; letter-spacing: 6px; margin-right: -6px; color: var(--ink); }
  .edge-author {
    left: 402px; top: 509px; width: 150px; height: 16px;
    transform: rotate(90deg); font-family: "Poppins", sans-serif; font-weight: 300;
    font-size: 15px; line-height: 16px; text-align: center; color: var(--ink);
  }

  /* front */
  .front-author {
    left: -6px; top: 97px; width: 120px; height: 16px;
    transform: rotate(-90deg); font-family: "Poppins", sans-serif; font-weight: 300;
    font-size: 12px; line-height: 16px; text-align: center; color: var(--white);
  }
  .front-title { left: 58px; top: 350px; width: 313px; text-align: right; }
  .front-title .article { font-size: 14px; line-height: 18px; color: var(--white); margin-right: -5px; }
  .front-title .main { font-size: 64px; line-height: 66px; color: var(--white); }
  .front-title .second { font-size: 18px; line-height: 22px; letter-spacing: 8px; margin-right: -8px; color: var(--sky); }
  .tagline {
    left: 0; top: 537px; width: 434px; text-align: center; color: var(--white);
    font-family: "Poppins", sans-serif; font-size: 11.5px; line-height: 14.5px; letter-spacing: 2.4px;
  }
  .tagline b { font-family: "Montserrat", sans-serif; font-weight: 700; font-style: italic; }
</style>
</head>
<body>
<main class="spread">
  <section class="back-cover">
    <div class="abs house-art" role="img" aria-label="Soft illustration of a model house with rolled blueprints"></div>

    <h2 class="abs lockup back-title">
      <span class="article">THE</span>
      <span class="main">QUIET</span>
      <span class="second">LANDLORD</span>
    </h2>

    <div class="abs copy">
      <p class="lead">What if the smartest property investors in the world don’t actually own anything?</p>
      <p>In a world where leverage has replaced labor and access has replaced assets, The Quiet Landlord reveals how a new generation of entrepreneurs is building wealth without deeds, mortgages, or massive capital.</p>
      <p>Mel T. Varnak exposes the hidden playbook behind modern property wealth — not through ownership, but through control, creativity, and influence</p>
      <p class="lead">You’ll discover how to:</p>
      <ul class="benefits">
        <li><span class="hl">Profit from properties you never buy</span> through partnerships, performance models, and control agreements.</li>
        <li><span class="hl">Monetize your skills, systems, and relationships</span> just like institutional investors do.</li>
        <li><span class="hl">Build digital real estate —</span> brands, websites, and lead funnels that pay like rentals.</li>
        <li><span class="hl">Create recurring income</span> through master leases, management contracts, and service-based equity.</li>
        <li><span class="hl">Design your freedom formula —</span> where wealth is measured in time, not titles.</li>
      </ul>
      <p>Packed with frameworks, examples, and the mindset of modern deal-makers, The Quiet Landlord is a blueprint for the future of wealth creation — one built on access, not assets.</p>
      <p class="gap">Because in the new economy, <strong>the most powerful investors don’t own property.<br>They own opportunity.</strong></p>
      <p><strong>And now, you can too.</strong></p>
    </div>

    <div class="abs author-photo"><div role="img" aria-label="Author portrait in a dark blazer, indoor office setting"></div></div>
    <div class="abs about-label">About the Author</div>
    <p class="abs bio"><strong>Mel T. Varnak</strong> is a property entrepreneur and owner of Halvern Studio in Las Vegas, NV and Keystone Realty Partners in Ventura, California. Combining design, development, and deal strategy, he’s helped agents, investors, and entrepreneurs build freedom through systems — not stuff. The Quiet Landlord is his definitive guide to building wealth through creative control.</p>

    <div class="abs lockup edge-title">
      <div class="row"><span class="article">THE</span><span class="main">QUIET</span></div>
      <span class="second">LANDLORD</span>
    </div>
    <div class="abs edge-author">by Mel T. Varnak</div>
  </section>

  <section class="front-cover" role="img" aria-label="Moody photo of a man in a fedora and tweed coat, face hidden in shadow, on a dark blue backdrop">
    <div class="abs front-author">by Mel T. Varnak</div>
    <h1 class="abs lockup front-title">
      <span class="article">THE</span>
      <span class="main">QUIET</span>
      <span class="second">LANDLORD</span>
    </h1>
    <p class="abs tagline">How to <b>Grow Comfort</b> and <b>Plenty</b><br>Through Property<br>Held by Others</p>
  </section>
</main>
</body>
</html>
```